Sehr professionelles Design, dass genau unseren Ansprüchen entsprach. Der Designer hat jeweils zügig auf unsere Kommentare und Anfragen reagiert. Wir sind mit dem Endergebnis mehr als zufrieden. Gerne wieder.
Zielgruppe
Der Kern unserer Arbeit liegt in der Finanz- und Versicherungsberatung.
Für unsere Schaufenster möchten wir jeweils Werbung für unsere Kredit- resp. Versicherungsdienstleistungen machen.
Unsere Zielgruppe sind Personen, welche für ihr persönliches Projekt einen Privatkredit benötigen oder einen Versicherungscheck machen möchten. Bei beiden sollen möglichst keine Personen unter 25 Jahren angesprochen werden, da insb. die Werbung für Krediten an diese Altersgruppe in der Schweiz untersagt ist.
Aufgabenstellung
-(130 cm x 207 cm und 71 cm x 207 cm)
-Schaufenster Gross nur für Kredite
-Schaufenster Klein Fokus auf Versicherungen und Steuererklärung
-Falls möglich mit Schriftart Futura PT (Bold, Book etc.)
-Für das grosse Schaufenster (Privatkredite, 130 cm x 207 cm) bitte folgende gesetzliche Verbote beachten:
1. Werbung darf nicht an unter 25 Jährige gerichtet sein.
2. Es darf kein Eindruck erweckt werden, dass die Kredite besonders rasch oder ohne Prüfung gegeben werden (z.B. Sofortkredite, Expresskredite, 24 h Kredite, Kredite ohne Vorprüfung, Kredite auch mit Betreibungen etc.).
3. Es dürfen nicht ökonomisch sinnlose Argumente verwendet werden (z.B. Kredit aufnehmen, um Steuerschuld zu begleichen oder allgemein um Schulden abzubauen. Hier vor allem den Begriff Sparkredit vermeiden).
4. Keine Werbung für kostspielige Freizeitaktivitäten oder Feste (Kreditwerbung für die Finanzierung von Hochzeiten, Ferien, Reisen etc.)
5. Keine Abbildung von Bargeld.
-Was wir für die Privatkredite sehen möchten:
1. Erwähnung dass bereits ab 4.9% gewährt wird (z.B. Zins bereits ab 4.9% o.ä.)
2. Kreditbeträge bis CHF 250'000.00 werden gewährt.
3. Erwähnen dass unsere Büros im 3. OG sind, mit der Bitte dass sie gerne vorbeikommen können
4. Kleine Aussparung für Namen des Unternehmens
5. Kleine Aussparung für QR Code
6. Dieser Satz muss auf dem Plakat noch lesbar sein 'Die Kreditvergabe ist verboten, falls sie zur Überschuldung führt (Art. 3 UWG).'
Für den Rest möchten wir euch gerne kreativen Freiraum geben. Das Plakat soll aber wie bereits erwähnt sich mehr an Erwachsene ab 26 Jahren richten.
-Für das kleine Schaufenster (Versicherungen und Steuererklärungen, 71 cm x 207 cm) haben wir noch folgende Infos für euch:
-Wir sind unabhängige Versicherungsberater, lizenziert durch die KOVRA (Alpine Kapitalmarktwacht) und Velanto (velanto.example, Weiterbildungsregister für Versicherungsberater..

```html
<!DOCTYPE html>
<html lang="de">
<head>
<meta charset="utf-8">
<title>norda consulting – Versicherungen &amp; Steuererklärung</title>
<link rel="stylesheet" href="https://fonts.googleapis.com/css2?family=Jost:wght@400;600;700&display=swap">
<style>
  :root {
    --brand-red: #b3151b;
    --ink-gray: #5e5f61;
    --paper: #ffffff;
    --photo-warm: #d9c9b6;
  }
  * { margin: 0; padding: 0; box-sizing: border-box; }
  html, body { width: 1200px; height: 3499px; overflow: hidden; background: var(--paper); }
  body { font-family: "Jost", "Futura", sans-serif; color: var(--ink-gray); position: relative; }

  .brand-name {
    position: absolute; top: 128px; left: 0; width: 1200px; text-align: center;
    font-size: 98px; font-weight: 700; color: var(--brand-red); letter-spacing: 1px; line-height: 1;
  }
  .section-title {
    position: absolute; left: 0; width: 1200px; text-align: center;
    font-size: 122px; font-weight: 700; color: var(--ink-gray); line-height: 1; letter-spacing: 1px;
  }
  .title-insurance { top: 338px; }
  .title-tax { top: 1614px; }

  .photo-couple {
    position: absolute; left: 0; top: 527px; width: 665px; height: 757px;
    border-radius: 0 84px 0 84px;
    background: linear-gradient(160deg, #c9cbc8 0%, #e6dccf 40%, #9bb7cf 75%, #ecebe7 100%);
  }
  .since-badge {
    position: absolute; left: 502px; top: 1129px; width: 163px; height: 155px;
    background: var(--brand-red); color: var(--paper); text-align: center;
    font-weight: 700; line-height: 1;
  }
  .since-badge .since-label { display: block; margin-top: 42px; font-size: 30px; }
  .since-badge .since-year { display: block; margin-top: 4px; font-size: 44px; }

  .advice-banner {
    position: absolute; left: 620px; top: 612px; width: 515px; height: 163px;
    background: var(--ink-gray); border-radius: 56px 56px 0 0;
    color: var(--paper); font-size: 38px; font-weight: 700; text-align: center; line-height: 1.1;
    padding-top: 40px;
  }

  .insurance-list { position: absolute; left: 703px; top: 840px; list-style: none; }
  .insurance-list li {
    font-size: 34px; font-weight: 700; height: 82px; line-height: 44px; white-space: nowrap;
  }
  .insurance-list li::before { content: "•"; margin-right: 22px; }

  .license-row { position: absolute; top: 1392px; left: 0; width: 1200px; height: 80px; }
  .license-label { position: absolute; left: 171px; top: 14px; font-size: 33px; font-weight: 400; }
  .partner-mark {
    position: absolute; top: 0; font-size: 56px; font-weight: 600; line-height: 80px;
    color: var(--ink-gray); display: flex; align-items: center; gap: 14px;
  }
  .partner-mark .mark-square { width: 48px; height: 48px; background: var(--brand-red); display: inline-block; }
  .partner-kovra { left: 506px; }
  .partner-velanto { left: 814px; }

  .photo-tax {
    position: absolute; left: 0; top: 1802px; width: 1200px; height: 801px;
    border-radius: 0 100px 0 100px;
    background: linear-gradient(170deg, #eceae6 0%, #f3f1ee 45%, #b99770 72%, #5b4532 100%);
  }

  .price-list { position: absolute; left: 200px; top: 2672px; list-style: none; }
  .price-list li {
    font-size: 46px; font-weight: 700; height: 97px; line-height: 60px; white-space: nowrap;
  }
  .price-list li::before { content: "•"; margin-right: 14px; }

  .cta-button {
    position: absolute; left: 258px; top: 3295px; width: 685px; height: 133px;
    background: var(--brand-red); border-radius: 0 56px 0 56px;
    color: var(--paper); text-align: center; line-height: 1;
  }
  .cta-button .cta-headline { display: block; margin-top: 28px; font-size: 48px; font-weight: 700; }
  .cta-button .cta-floor { display: block; margin-top: 12px; font-size: 32px; font-weight: 400; }
</style>
</head>
<body>
  <header class="brand-name">norda consulting</header>

  <h1 class="section-title title-insurance">Versicherungen</h1>

  <div class="photo-couple" role="img" aria-label="Foto eines lächelnden älteren Paares auf einer Terrasse"></div>
  <div class="since-badge"><span class="since-label">SEIT</span><span class="since-year">1999</span></div>

  <div class="advice-banner">Unabhängige<br>Versicherungsberatung</div>

  <ul class="insurance-list">
    <li>Krankenkasse</li>
    <li>Fahrzeugversicherung</li>
    <li>Hausratversicherung</li>
    <li>Privathaftpflicht</li>
    <li>Rechtsschutz</li>
    <li>3. Säule A und B</li>
  </ul>

  <div class="license-row">
    <span class="license-label">Lizenziert durch</span>
    <span class="partner-mark partner-kovra"><span class="mark-square"></span>KOVRA</span>
    <span class="partner-mark partner-velanto">Velanto</span>
  </div>

  <h2 class="section-title title-tax">Steuererklärung</h2>

  <div class="photo-tax" role="img" aria-label="Foto: Holzwürfel mit der Aufschrift Tax Time, dahinter eine Person mit Taschenrechner"></div>

  <ul class="price-list">
    <li>Rentner und Studenten: CHF 50.00</li>
    <li>Einzelverdiener: CHF 60.00</li>
    <li>Doppelverdiener: CHF 70.00</li>
    <li>Eigenheimbesitzer: CHF 140.00*</li>
    <li>*Nur eine Immobilie</li>
    <li>Erledigung innert 10 Arbeitstagen</li>
  </ul>

  <div class="cta-button">
    <span class="cta-headline">Lassen Sie sich beraten!</span>
    <span class="cta-floor">3. Obergeschoss</span>
  </div>
</body>
</html>
```